Multiple Packaging Solutions for LED bulbs

We need a packaging design for led bulbs for our company. We need something that can be easily adjusted in different packaging types, as we have multiple different products. It needs to be fresh, friendly, happy but at the same time corporate. We provide some basic packaging dimensions and also our logo in the respective files. The packaging could be of plastic/trasparent, or carton (regular or ecofriendly)

Industry/Entity Type

It Company

```html
<!DOCTYPE html>
<html lang="en">
<head>
<meta charset="utf-8">
<title>Lumivo LED Bulb Packaging</title>
<link href="https://fonts.googleapis.com/css2?family=Exo+2:wght@200;300;600;700;800&display=swap" rel="stylesheet">
<style>
  :root{
    --stage:#d9d9d9;
    --night:#120c2e;
    --violet:#3a1f7a;
    --glow:#6a55d8;
    --orange:#e8731c;
    --orange-dark:#b94a0c;
    --red:#c0301c;
    --white:#ffffff;
    --bulb-light:#f2f2f0;
    --bulb-mid:#b9bcc0;
  }
  *{box-sizing:border-box;margin:0;padding:0}
  html,body{width:1200px;height:989px;overflow:hidden}
  body{background:var(--stage);font-family:"Exo 2",sans-serif;color:var(--white);position:relative}

  .hang-tab{position:absolute;left:490px;top:60px;width:460px;height:140px;
    background:linear-gradient(160deg,var(--violet),var(--night) 70%);border-radius:4px 4px 0 0}
  .hang-tab .hole{position:absolute;left:160px;top:28px;width:140px;height:36px;border-radius:18px;background:var(--stage)}
  .hang-tab .brand{position:absolute;left:150px;top:88px}

  .panel{position:absolute;top:200px;height:700px;overflow:hidden}
  .panel-side{left:250px;width:240px;border-right:1px solid rgba(0,0,0,.4)}
  .panel-front{left:490px;width:460px}
  .backdrop{position:absolute;inset:0;
    background:radial-gradient(ellipse at 55% 45%,var(--glow) 0%,var(--violet) 35%,var(--night) 80%)}

  .brand{display:flex;align-items:center;gap:12px;font-weight:300;font-size:38px;letter-spacing:.5px;color:var(--white)}
  .brand .dot{width:26px;height:26px;border-radius:50%;background:var(--orange)}

  .panel-side .brand{position:absolute;left:24px;top:40px;font-size:32px}
  .panel-front .brand{position:absolute;left:100px;top:40px}

  .tag{position:absolute;background:linear-gradient(180deg,var(--orange),var(--orange-dark));
    font-weight:700;color:var(--white);display:flex;align-items:center;white-space:nowrap}
  .tag-dimmable{left:0;top:170px;width:200px;height:60px;padding-left:20px;font-size:24px;
    clip-path:polygon(0 0,100% 0,88% 100%,0 100%)}
  .tag-watts{right:0;top:400px;width:160px;height:80px;padding-left:34px;font-size:22px;gap:6px;
    clip-path:polygon(12% 0,100% 0,100% 100%,0 100%)}
  .tag-watts b{font-size:48px;font-weight:800}

  .headline{position:absolute;right:30px;top:170px;display:flex;align-items:flex-end;gap:8px}
  .headline .small{text-align:right;font-weight:700;font-size:30px;line-height:1;text-transform:uppercase}
  .headline .small .a{color:var(--orange)}
  .headline .small .b{color:var(--red)}
  .headline .big{font-weight:200;font-size:96px;line-height:.82}

  .bulbs{position:absolute;left:70px;top:290px;width:290px;height:390px;border-radius:50% 50% 10% 10%/40% 40% 10% 10%;
    background:linear-gradient(180deg,var(--bulb-light) 0%,var(--bulb-light) 35%,var(--bulb-mid) 65%,#8e9196 100%)}

  .lumens{position:absolute;right:30px;bottom:50px;text-align:center}
  .lumens .num{font-weight:700;font-size:76px;line-height:1}
  .lumens .unit{font-weight:600;font-size:22px;letter-spacing:1px}

  .side-label{position:absolute;left:26px;bottom:60px;line-height:1}
  .side-label .a{color:var(--orange);font-weight:700;font-size:30px}
  .side-label .big{font-weight:200;font-size:110px;line-height:.9}
  .side-label .b{color:var(--red);font-weight:700;font-size:26px}
</style>
</head>
<body>
  <section class="hang-tab">
    <div class="hole"></div>
    <div class="brand"><span class="dot"></span>Lumivo</div>
  </section>

  <section class="panel panel-side">
    <div class="backdrop" role="img" aria-label="Purple electric lightning texture background"></div>
    <div class="brand"><span class="dot"></span>Lumivo</div>
    <div class="tag tag-dimmable">DIMMABLE</div>
    <div class="side-label">
      <div class="a">LONG-LIFE</div>
      <div class="big">LED</div>
      <div class="b">BULB</div>
    </div>
  </section>

  <section class="panel panel-front">
    <div class="backdrop" role="img" aria-label="Purple electric lightning texture background"></div>
    <div class="brand"><span class="dot"></span>Lumivo</div>
    <div class="headline">
      <div class="small"><div class="a">LONG-LIFE</div><div class="b">BULB</div></div>
      <div class="big">LED</div>
    </div>
    <div class="bulbs" role="img" aria-label="Photo of three white LED bulbs with aluminium heat-sink bodies and screw bases"></div>
    <div class="tag tag-watts"><b>9</b>WATTS</div>
    <div class="lumens"><div class="num">550</div><div class="unit">LUMENS</div></div>
  </section>
</body>
</html>
```